VaultMeridan Business Card Re-Design

VaultMeridan is a specialized information security company that applies its proven methodology of security Assessment, Development, Integration and Training (A-D-I-T) to provide cyber security services in the areas of Data Protection, Network Defense and Compliance. We need the current business card re-designed to properly scale the fonts and possibly rearranging some elements (icons, lettering, etc.) to make the card more appealing to the eye. The card should have the logo that is on the web site (www.vaultmeridan-example.com). We would like ideas for both a black card (black background) and a white card (white background). We prefer rounded corners to help the card stand out but are open to all ideas. FYI: VaultMeridan's slogan is "...your security is our business".

Target Market(s)

#1 US Government Contracting Companies, #2 Commercial Companies, #3 Gen. Public.

Industry/Entity Type

Business

Contact Information for Business Card

See Description; open to the use of different fonts.

Font styles to use
Sans Serif

Colors
000000
ec1f27
ffffff

Requirements
Must have
• Company logo on web site, rounded corners, list of company offerings on the back of the card.
Nice to have
• Icons
Should not have
• none

```html
<!DOCTYPE html>
<html lang="en">
<head>
<meta charset="utf-8">
<title>VaultMeridan Business Card</title>
<link rel="stylesheet" href="https://fonts.googleapis.com/css2?family=Open+Sans:wght@400;600;700&display=swap">
<style>
  :root {
    --black: #000000;
    --card-black: #0b0b0b;
    --red: #ec1f27;
    --white: #ffffff;
    --paper: #eeeeee;
    --paper-edge: #d9d9d9;
    --ink: #2b2b2b;
    --muted: #cfcfcf;
    --stage: #e6e6e6;
  }
  * { box-sizing: border-box; margin: 0; padding: 0; }
  html, body {
    width: 1200px; height: 1120px; overflow: hidden;
    background: var(--stage);
    font-family: "Open Sans", Arial, sans-serif;
  }
  .canvas {
    width: 1200px; height: 1120px;
    display: flex; flex-direction: column; align-items: center;
    justify-content: center; gap: 30px;
  }
  .card {
    width: 900px; height: 514px; border-radius: 26px;
    overflow: hidden; position: relative;
    box-shadow: 0 10px 28px rgba(0,0,0,.22);
  }

  /* brand lockup */
  .brand { display: flex; flex-direction: column; align-items: center; text-align: center; }
  .brand-row { display: flex; align-items: center; gap: 16px; }
  .brand-dot { width: 22px; height: 22px; border-radius: 50%; background: var(--red); }
  .brand-name { color: var(--white); font-weight: 600; font-size: 46px; letter-spacing: 1px; }
  .brand-tag { color: var(--muted); font-size: 21px; margin-top: 14px; }

  /* back: services */
  .card-back { background: var(--card-black); }
  .card-back .brand { position: absolute; left: 0; top: 0; width: 390px; height: 430px; justify-content: center; }
  .card-back .divider {
    position: absolute; left: 400px; top: 50px; width: 2px; height: 340px;
    background: linear-gradient(#666, #999, #555);
  }
  .services {
    position: absolute; left: 436px; top: 46px; list-style: none;
    color: var(--white); font-size: 18.5px; line-height: 26.5px;
  }
  .services li { padding-left: 22px; position: relative; }
  .services li::before {
    content: ""; position: absolute; left: 2px; top: 10px;
    border-left: 6px solid transparent; border-right: 6px solid transparent;
    border-top: 8px solid var(--white);
  }
  .slogan {
    position: absolute; left: 0; right: 0; bottom: 44px; text-align: center;
    color: var(--white); font-size: 21px; letter-spacing: 1.5px;
  }

  /* front: contact */
  .card-front { display: flex; background: var(--paper); }
  .front-brand-panel {
    width: 400px; background: var(--card-black);
    display: flex; align-items: center; justify-content: center;
  }
  .front-brand-panel .brand-name { font-size: 42px; }
  .front-brand-panel .brand-tag { font-size: 20px; }
  .panel-edge { width: 12px; background: linear-gradient(90deg, #9a9a9a, #f4f4f4, #7c7c7c); }
  .contact-panel {
    flex: 1; padding: 60px 0 0 44px;
    background: linear-gradient(135deg, #f6f6f6, var(--paper-edge));
    color: var(--ink);
  }
  .person-name { font-size: 28px; font-weight: 700; color: #1e1e1e; }
  .person-role { font-size: 19px; margin-top: 2px; }
  .person-role .creds { color: var(--red); }
  .contact-list { list-style: none; margin-top: 30px; font-size: 20px; line-height: 30px; }
  .contact-list li { display: flex; align-items: center; gap: 12px; }
  .contact-list svg { width: 18px; height: 18px; flex: none; }
  .address { margin-top: 34px; font-size: 21px; line-height: 29px; }
</style>
</head>
<body>
<main class="canvas">

  <section class="card card-back" aria-label="Card back: services">
    <div class="brand">
      <div class="brand-row"><span class="brand-dot"></span><span class="brand-name">VaultMeridan</span></div>
      <p class="brand-tag">Information Security Solutions</p>
    </div>
    <div class="divider"></div>
    <ul class="services">
      <li>Secure Cloud &amp; Open Stack Solutions</li>
      <li>Network Attack Penetration &amp; Defense</li>
      <li>Red/Blue Team</li>
      <li>Data Center Consolidation</li>
      <li>Secure Virtual Computing</li>
      <li>Classified Cross Domain Solutions</li>
      <li>Foreign/Counter Intelligence Data Security</li>
      <li>Certification &amp; Accreditation</li>
      <li>Secure Wireless Solutions</li>
      <li>Security Training, Assessment &amp; Integration</li>
      <li>Security Subject Matter Experts</li>
      <li>Executive Security Strategy Coaching</li>
      <li>Data Encryption/Privacy</li>
    </ul>
    <p class="slogan">YOUR SECURITY IS OUR BUSINESS</p>
  </section>

  <section class="card card-front" aria-label="Card front: contact">
    <div class="front-brand-panel">
      <div class="brand">
        <div class="brand-row"><span class="brand-dot"></span><span class="brand-name">VaultMeridan</span></div>
        <p class="brand-tag">Information Security Solutions</p>
      </div>
    </div>
    <div class="panel-edge"></div>
    <div class="contact-panel">
      <h1 class="person-name">Daniel Reyes</h1>
      <p class="person-role">President - CEO, <span class="creds">CISSP, CEH</span></p>
      <ul class="contact-list">
        <li>
          <svg viewBox="0 0 20 20"><circle cx="10" cy="10" r="10" fill="#ec1f27"/><path d="M6 5.5c0 5 3.5 9 8.5 9l.5-2.5-2.5-1-1 1.2c-1.5-.7-2.6-1.8-3.2-3.2l1.2-1-1-2.5z" fill="#fff"/></svg>
          <span>555-010-1201</span>
        </li>
        <li>
          <svg viewBox="0 0 20 20"><rect x="5" y="2" width="10" height="16" rx="2" fill="#ec1f27"/><rect x="7" y="4.5" width="6" height="8" fill="#fff"/><circle cx="10" cy="15.3" r="1" fill="#fff"/></svg>
          <span>555-010-1627</span>
        </li>
        <li>
          <svg viewBox="0 0 20 20"><rect x="1" y="4" width="18" height="13" rx="2" fill="#ec1f27"/><path d="M3 6.5l7 5 7-5" fill="none" stroke="#fff" stroke-width="1.6"/></svg>
          <span>info@vaultmeridan-example.com</span>
        </li>
        <li>
          <svg viewBox="0 0 20 20"><rect x="1" y="4" width="18" height="13" rx="2" fill="#ec1f27"/><path d="M3 6.5l7 5 7-5" fill="none" stroke="#fff" stroke-width="1.6"/></svg>
          <span>dreyes@vaultmeridan-example.com</span>
        </li>
        <li>
          <svg viewBox="0 0 20 20"><circle cx="10" cy="10" r="9" fill="#ec1f27"/><g fill="none" stroke="#fff" stroke-width="1.2"><circle cx="10" cy="10" r="6.5"/><ellipse cx="10" cy="10" rx="3" ry="6.5"/><path d="M3.5 10h13"/></g></svg>
          <span>www.vaultmeridan-example.com</span>
        </li>
      </ul>
      <address class="address" style="font-style:normal">
        VaultMeridan, Inc.<br>
        4170 Harlow Ave. Suite 210<br>
        Rockridge, Maryland 20999
      </address>
    </div>
  </section>

</main>
</body>
</html>
```